MARLOW CREST WINE LABEL DESIGN PROJECT

We need an elegant wine label design for our new range of wine. We need 3 labels for the range

2015 MARLOW CREST SHIRAZ
2015 MARLOW CREST CABERNET SAUVIGNON
2015 MARLOW CREST CABERNET SHIRAZ

The Size is nominated at 120mm High x 90mm Wide (Front and Back) but we are open to creative expression even if size differs

We are open to any style of label and designer can work on their strengths. it can be modern/classic/old fashion etc

I have attached the marlow crest logo ( the 2 olives) and a set up called wine mandatories which is in no way a design direction just the mandatory info that needs to appear on labels. The wine mandatories is just the information that needs to go on the label it has nothing to do with the design. DO not make designs based on this at all. These labels are for red wine not olive oil.

I have also attached some of the companies current olive oil labels ( TORQUALE AND WANDELLA AND MARLOW CREST so you can see other labels and how this wine product will sit in gift baskets.

Thanks
Tomasz.

Reason: Hello Friends We have decided to extend the deadline to enable more submissions. Many of the designs submitted have images of olives and look like olive oil product. We only need the olive logo to be shown on the label but the rest of the design should be a classic simple red wine label. It is not olive oil or olive product - it is red wine. Please keep simple and stylish Thanks Tomasz

Target Market(s)

35-65

Font styles to use
Serif

Requirements
Must have
• AS per brief
Nice to have
• as per brief
Should not have
• as per brief

```html
<!DOCTYPE html>
<html lang="en">
<head>
<meta charset="utf-8">
<title>The Marlow Crest – Lower Murray Shiraz Label</title>
<link href="https://fonts.googleapis.com/css2?family=Josefin+Sans:wght@300;400;600&display=swap" rel="stylesheet">
<style>
  :root {
    --backdrop: #141414;
    --paper-light: #f1f1ef;
    --paper-mid: #d9d9d7;
    --paper-shade: #c4c4c2;
    --olive-green: #566b2a;
    --ink: #121212;
    --band-text: #f4f4ee;
    --olive-purple: #4e2c42;
  }
  * { box-sizing: border-box; margin: 0; padding: 0; }
  html, body {
    width: 1200px; height: 1200px; overflow: hidden;
    background: var(--backdrop);
    font-family: "Josefin Sans", "Futura", sans-serif;
  }
  .label {
    position: absolute; left: 220px; top: 100px;
    width: 760px; height: 1000px;
    background:
      radial-gradient(ellipse at 30% 35%, rgba(255,255,255,0.55), transparent 60%),
      radial-gradient(ellipse at 80% 70%, rgba(150,150,150,0.35), transparent 55%),
      linear-gradient(160deg, var(--paper-light) 0%, var(--paper-mid) 55%, var(--paper-shade) 100%);
  }
  .label__frame {
    position: absolute; left: 30px; top: 30px; right: 30px; bottom: 30px;
    border: 8px solid var(--olive-green);
  }
  .label__brand {
    position: absolute; top: 100px; left: 40px; right: 40px;
    text-align: center; color: var(--ink);
    font-weight: 400; font-size: 56px; letter-spacing: 0.05em;
    white-space: nowrap; line-height: 1;
  }
  .label__tagline {
    position: absolute; top: 180px; left: 0; right: 0;
    text-align: center; color: var(--ink);
    font-weight: 400; font-size: 26px; letter-spacing: 0.12em;
    white-space: nowrap; line-height: 1;
  }
  .label__mark {
    position: absolute; top: 390px; left: 0; right: 0;
    display: flex; align-items: center; justify-content: center; gap: 22px;
  }
  .label__mark-dot {
    width: 64px; height: 64px; border-radius: 50%;
    background: var(--olive-purple);
  }
  .label__mark-name {
    color: var(--olive-green);
    font-weight: 400; font-size: 44px; letter-spacing: 0.1em;
    white-space: nowrap;
  }
  .label__vintage {
    position: absolute; top: 650px; right: 130px;
    color: var(--ink); font-weight: 400; font-size: 62px; letter-spacing: 0.12em;
    line-height: 1;
  }
  .label__region {
    position: absolute; top: 725px; left: 0; right: 0; height: 80px;
    background: var(--olive-green);
    color: var(--band-text);
    font-weight: 400; font-size: 58px; letter-spacing: 0.06em;
    display: flex; align-items: center; padding-left: 70px; padding-top: 8px;
    white-space: nowrap;
  }
  .label__variety {
    position: absolute; top: 835px; left: 0; right: 0;
    text-align: center; color: var(--ink);
    font-weight: 400; font-size: 46px; letter-spacing: 0.55em;
    line-height: 1;
  }
  .label__volume, .label__alcohol {
    position: absolute; left: 0; right: 0; text-align: center;
    color: var(--ink); font-weight: 600; font-size: 22px; letter-spacing: 0.08em;
    line-height: 1;
  }
  .label__volume { top: 900px; }
  .label__alcohol { top: 934px; }
</style>
</head>
<body>
  <main class="label">
    <div class="label__frame"></div>
    <h1 class="label__brand">THE MARLOW CREST</h1>
    <p class="label__tagline">PREMIUM AUSTRALIAN WINE</p>
    <div class="label__mark">
      <span class="label__mark-dot"></span>
      <span class="label__mark-name">MARLOW CREST</span>
    </div>
    <p class="label__vintage">2015</p>
    <p class="label__region">LOWER MURRAY</p>
    <p class="label__variety">SHIRAZ</p>
    <p class="label__volume">750ML</p>
    <p class="label__alcohol">14,5% ALC/VOL</p>
  </main>
</body>
</html>
```